Upmarket Bathroom and Kitchen ware supplier needs a classy business card design

We are a company based in Fiji, we sell plumbing ware (Kitchen and bathroom taps, Basins,showers, toilets etc) through up market show rooms to individuals and directly through Architects and designers of resorts and holiday houses for new builds and renovations. we are wanting to upgrade our over all look and brand. we are starting with a new logo but will be rebranding the whole business. This project is for a business card design for my management and tales team I would like it to be dark, classy and interesting

Target Market(s)

Resort directors and Management, High end holiday home owners

Contact Information for Business Card

Neil Dawson
Director
+64219473815

Colors

Designer to choose colors to be used in the design.

Requirements
Must have
• Must have an upmarket appearance I like darker charcoal shades but will be guided by the designers
• Please any catch phrases like "Crafting remarkable living rooms" this belongs tpo one of our suppliers so can not be used.
Nice to have
• Double sided, so front dedicated to logo provided and back info about the business and the person.

```html
<!DOCTYPE html>
<html lang="en">
<head>
<meta charset="utf-8">
<title>Lagoon Interiors — Business Card</title>
<link rel="stylesheet" href="https://fonts.googleapis.com/css2?family=Montserrat:wght@300&family=Open+Sans:wght@400;700&display=swap">
<style>
  :root {
    --backdrop: #2b2e33;
    --card: #111214;
    --card-edge: #1c1d20;
    --ink: #f2f2f2;
    --ink-muted: #c9c9c9;
    --rule: #8a8a8a;
  }
  * { margin: 0; padding: 0; box-sizing: border-box; }
  html, body { width: 1200px; height: 900px; overflow: hidden; }
  body {
    background: radial-gradient(ellipse at 40% 35%, #3a3e44 0%, var(--backdrop) 55%, #1d1f22 100%);
    position: relative;
    font-family: "Open Sans", sans-serif;
  }
  .card {
    position: absolute;
    width: 560px;
    height: 320px;
    background: linear-gradient(160deg, #1a1b1e 0%, var(--card) 60%);
    border: 1px solid var(--card-edge);
    border-radius: 4px;
    box-shadow: 0 24px 50px rgba(0,0,0,.55);
  }
  /* Front: brand name */
  .card--front { left: 580px; top: 110px; }
  .brand {
    position: absolute;
    left: 0; right: 0; top: 50%;
    transform: translateY(-50%);
    text-align: center;
    font-family: "Montserrat", sans-serif;
    font-weight: 300;
    font-size: 30px;
    letter-spacing: 10px;
    color: var(--ink);
  }
  /* Back: person + contact */
  .card--back { left: 60px; top: 470px; }
  .identity {
    position: absolute;
    left: 40px; top: 112px;
    width: 190px;
    text-align: right;
  }
  .identity__name {
    font-weight: 700;
    font-size: 22px;
    letter-spacing: 1px;
    color: var(--ink);
  }
  .identity__role {
    font-size: 16px;
    color: var(--ink-muted);
  }
  .divider {
    position: absolute;
    left: 250px; top: 100px;
    width: 1px; height: 120px;
    background: var(--rule);
  }
  .contact {
    position: absolute;
    left: 268px; top: 104px;
    list-style: none;
  }
  .contact__item {
    display: flex;
    align-items: center;
    gap: 10px;
    height: 36px;
    font-size: 17px;
    color: var(--ink-muted);
  }
  .contact__item strong { color: var(--ink); font-weight: 700; }
  .contact__icon { width: 16px; height: 16px; flex: none; fill: var(--ink); }
</style>
</head>
<body>
  <section class="card card--front" aria-label="Card front">
    <div class="brand">LAGOON INTERIORS</div>
  </section>

  <section class="card card--back" aria-label="Card back">
    <div class="identity">
      <div class="identity__name">NEIL DAWSON</div>
      <div class="identity__role">Director</div>
    </div>
    <div class="divider"></div>
    <ul class="contact">
      <li class="contact__item">
        <svg class="contact__icon" viewBox="0 0 16 16" aria-hidden="true"><path d="M3.2 1.5l2.3 2.6-1.4 1.6c.9 2 2.4 3.5 4.4 4.4l1.6-1.4 2.6 2.3-1.5 2c-5.3-.4-9.4-4.5-9.8-9.8z"/></svg>
        <span>+642 1947 3815</span>
      </li>
      <li class="contact__item">
        <svg class="contact__icon" viewBox="0 0 16 16" aria-hidden="true"><path d="M1 3h14v10H1z M2.5 4.5v.3L8 8.6l5.5-3.8v-.3z" fill-rule="evenodd"/></svg>
        <span>info@lagooninteriors.com</span>
      </li>
      <li class="contact__item">
        <svg class="contact__icon" viewBox="0 0 16 16" aria-hidden="true"><path d="M8 1a7 7 0 100 14A7 7 0 008 1zm0 1.3c.8 0 1.7 1.6 2 4H6c.3-2.4 1.2-4 2-4zM2.4 7.3h2.3c0-1.6.3-3 .8-4a5.7 5.7 0 00-3.1 4zm0 1.4a5.7 5.7 0 003.1 4c-.5-1-.8-2.4-.8-4zm3.6 0h4c-.3 2.4-1.2 4-2 4s-1.7-1.6-2-4zm5.3 0c0 1.6-.3 3-.8 4a5.7 5.7 0 003.1-4zm2.3-1.4a5.7 5.7 0 00-3.1-4c.5 1 .8 2.4.8 4z"/></svg>
        <span>www.<strong>lagooninteriors</strong>.com</span>
      </li>
    </ul>
  </section>
</body>
</html>
```